Corvane Project Services - Flyer

Project Breif:
I need a single page A4 Capability Statement, which will be used to market our services to prospective clients, both in print and via email PDF.
It needs to look professional and should incorporate the elements I have uploaded into files, these include:
Capability Statement Text
Corvane Services Company Logo
Additional Logo’s (Tools We Use)
Glimmer Bay Pics can be cut into the page
I have included examples of capability statements as a guide to what i am looking for.
Regards
Derek
Engineering Consulting

```html
<!DOCTYPE html>
<html lang="en">
<head>
<meta charset="utf-8">
<title>Corvane Project Services – Capability Statement</title>
<link href="https://fonts.googleapis.com/css2?family=Quicksand:wght@400;500;700&display=swap" rel="stylesheet">
<style>
  :root {
    --backdrop: #e6ebf0;
    --paper: #ffffff;
    --brand-blue: #1747b0;
    --teal: #1a9cc4;
    --ink: #2f3a45;
    --ink-soft: #5b6672;
    --rule: #cfd6de;
    --panel: #f3f6f9;
  }
  * { box-sizing: border-box; margin: 0; padding: 0; }
  html, body { width: 1200px; height: 859px; overflow: hidden; }
  body {
    background: var(--backdrop);
    font-family: "Quicksand", sans-serif;
    color: var(--ink);
  }
  .flyer {
    position: absolute;
    left: 317px; top: 29px;
    width: 566px; height: 800px;
    background: var(--paper);
    border-top: 4px solid var(--brand-blue);
    box-shadow: 0 10px 30px rgba(40,60,90,.18);
    overflow: hidden;
  }
  .flyer-header {
    height: 86px;
    display: flex; justify-content: space-between; align-items: center;
    padding: 0 30px;
  }
  .brand { display: flex; align-items: center; gap: 8px; }
  .brand-dot { width: 22px; height: 22px; border-radius: 50%; background: var(--brand-blue); }
  .brand-name {
    font-weight: 700; font-size: 12px; letter-spacing: .5px;
    color: var(--brand-blue); text-transform: uppercase; line-height: 1.2;
    width: 120px;
  }
  .doc-title { text-align: right; }
  .doc-title h1 { font-size: 26px; font-weight: 700; color: #1b1f24; }
  .doc-title p { font-size: 18px; color: var(--ink-soft); }
  .hero-image {
    height: 150px;
    background: linear-gradient(100deg, #eef2f6 0%, #dfe7ef 40%, #c9d6e4 70%, #e9eef3 100%);
  }
  .body { display: flex; padding: 22px 30px 0; height: 420px; }
  .intro { width: 52%; padding-right: 20px; border-right: 1px solid var(--rule); }
  .intro h2 {
    color: var(--teal); font-size: 18px; font-weight: 700; line-height: 1.25;
    margin-bottom: 14px;
  }
  .intro p { font-size: 9.5px; line-height: 1.5; color: var(--ink-soft); margin-bottom: 9px; }
  .intro-photo {
    margin-top: 12px; height: 110px;
    background: linear-gradient(135deg, #dbe5ef, #b9c9da 60%, #e4ebf2);
  }
  .services { width: 48%; padding-left: 20px; }
  .services h2 { color: var(--teal); font-size: 18px; font-weight: 700; margin-bottom: 8px; }
  .service-group { margin-bottom: 10px; }
  .service-group h3 { font-size: 9.5px; font-weight: 700; color: var(--ink); margin-bottom: 2px; }
  .service-group li { font-size: 9px; line-height: 1.45; color: var(--ink-soft); list-style: none; }
  .service-group li::before { content: "• "; color: var(--ink); }
  .contact h2 { color: var(--teal); font-size: 18px; font-weight: 700; margin: 8px 0 4px; }
  .contact p { font-size: 9px; line-height: 1.5; color: var(--ink-soft); }
  .contact strong { color: var(--ink); }
  .footer-band {
    position: absolute; left: 0; right: 0; bottom: 0; height: 92px;
    background: var(--brand-blue);
    display: flex; justify-content: space-between; align-items: flex-end;
    padding: 0 30px 18px;
  }
  .footer-web { color: #fff; font-size: 11px; font-weight: 500; }
  .social { display: flex; gap: 8px; }
  .social span { width: 18px; height: 18px; border-radius: 50%; border: 1.5px solid #fff; }
</style>
</head>
<body>
  <article class="flyer">
    <header class="flyer-header">
      <div class="brand">
        <span class="brand-dot"></span>
        <span class="brand-name">Corvane Project Services</span>
      </div>
      <div class="doc-title">
        <h1>Capability Statement</h1>
        <p>Change Management</p>
      </div>
    </header>

    <div class="hero-image" role="img" aria-label="Photo of a printed project schedule chart with a pen"></div>

    <section class="body">
      <div class="intro">
        <h2>Corvane Project Services Ltd. Is A Leading Project Control Consultancy Based In Co Cork Ireland</h2>
        <p>For over 20 years we have been helping our clients to deliver complex projects and programs throughout mainland Europe.</p>
        <p>We are passionate about empower organisations to achieve their objectives, on time and on budget.</p>
        <p>We are continually innovating, evolving and learning, utilize the latest industry tools and techniques to deliver real value to our clients.</p>
        <p>We make successful project delivery more predictable and more dependable.</p>
        <div class="intro-photo" role="img" aria-label="Photo of a consultant reviewing project documents"></div>
      </div>

      <div class="services">
        <h2>Core Services</h2>
        <div class="service-group">
          <h3>Planning and Scheduling</h3>
          <ul>
            <li>Tender Planning</li>
            <li>Interactive Planning / Pull Planning</li>
            <li>EPCM Planning &amp; Scheduling</li>
            <li>Schedule Earned Value Management</li>
            <li>Independent Schedule Quality Assessment</li>
            <li>Schedule Risk Analysis (Monte Carlo)</li>
            <li>Training</li>
          </ul>
        </div>
        <div class="service-group">
          <h3>Management of Risk</h3>
          <ul>
            <li>Risk Management Policies &amp; Procedures</li>
            <li>Risk Management Strategy</li>
            <li>Risk Registers</li>
            <li>Risk Improvement Planning</li>
            <li>Risk Response and Communication</li>
            <li>Risk Management Training</li>
          </ul>
        </div>
        <div class="service-group">
          <h3>Cost Control</h3>
          <ul>
            <li>Estimating &amp; Forecasting</li>
            <li>Earned Value Analysis</li>
            <li>Progress Reporting</li>
            <li>Cost Risk Analysis</li>
          </ul>
        </div>
        <div class="contact">
          <h2>Contact Us:</h2>
          <p><strong>Derek Halloran</strong> (Managing Director)</p>
          <p>info@corvaneservices.ie</p>
          <p>www.corvaneservices.ie</p>
          <p>+353 (0)87 555 0142</p>
        </div>
      </div>
    </section>

    <footer class="footer-band">
      <span class="footer-web">www.corvaneservices.ie</span>
      <div class="social" aria-label="Social links">
        <span></span><span></span><span></span>
      </div>
    </footer>
  </article>
</body>
</html>
```